Brightwell Auto Care 4x9 Rack Card

Design a 4" wide by 9" tall rack card printed front and back using the copy, logo and images uploaded below. I am also uploading a current flyer so you can see the typestyles we use. I will get the exact name of the font for you ASAP. Also will be uploading some before and after pictures for the back of the rack card

Target Market(s)

Affluent consumers who need their car cleaned and detailed in a meticulous fashion

Requirements
Must have
• Under the logo, put the words...... Premium Steam Detailing & Ceramic Coating.........also put ther following wording on the front side: Get Steamed! We use steam to clean your vehicle helping save millions of gallons of water and protecting our rivers, streams and lakes from runoff.
Nice to have
• a screened back background of hexagons might be nice

```html
<!DOCTYPE html>
<html lang="en">
<head>
<meta charset="utf-8">
<title>Brightwell Auto Care – Rack Card</title>
<link href="https://fonts.googleapis.com/css2?family=Montserrat:wght@600;700;800&display=swap" rel="stylesheet">
<style>
  :root{
    --page:#e6e8ea;
    --blue:#4a80c3;
    --green:#74af57;
    --white:#ffffff;
    --shade:rgba(60,60,70,.35);
  }
  *{margin:0;padding:0;box-sizing:border-box}
  html,body{width:1200px;height:1000px;overflow:hidden;background:var(--page)}
  body{position:relative;font-family:"Montserrat",Arial,sans-serif}
  .side-label{position:absolute;top:111px;font-size:21px;font-weight:700;letter-spacing:.2px}
  .side-label--front{left:217px;color:var(--blue)}
  .side-label--back{left:663px;color:var(--green)}
  .card{position:absolute;top:142px;width:320px;height:718px;filter:drop-shadow(5px 6px 3px var(--shade))}
  .card--front{left:217px}
  .card--back{left:663px;top:141px}
  .card svg{display:block;width:320px;height:718px}
  .card text{font-family:"Montserrat",Arial,sans-serif}
  .paper{fill:var(--white)}
  .f-blue{fill:var(--blue)}
  .f-green{fill:var(--green)}
  .f-white{fill:var(--white)}
  .wordmark{font-weight:800;font-size:22px;letter-spacing:1px;fill:var(--green)}
  .tagline{font-weight:600;font-size:6.2px;fill:var(--green)}
  .headline{font-weight:800;font-size:27px;fill:var(--white)}
  .slogan{font-weight:800;font-size:21px;fill:var(--white)}
  .copy{font-weight:700;font-size:16.5px}
  .bar-title{font-weight:800;font-size:19px;fill:var(--white);letter-spacing:.3px}
  .bar-small{font-weight:800;font-size:12.5px;fill:var(--white)}
  .section-title{font-weight:800;font-size:19px;fill:var(--blue)}
  .tile-label{font-weight:800;font-size:19px;fill:var(--white)}
  .price{font-weight:800}
</style>
</head>
<body>

<div class="side-label side-label--front">FRONTSIDE</div>
<div class="side-label side-label--back">BACKSIDE</div>

<!-- FRONT OF CARD -->
<div class="card card--front">
<svg viewBox="0 0 560 1257" xmlns="http://www.w3.org/2000/svg">
  <defs>
    <linearGradient id="frontDetailerTone" x1="0" y1="0" x2="1" y2="1">
      <stop offset="0" stop-color="#7fa3cf"/>
      <stop offset=".5" stop-color="#3f6fb2"/>
      <stop offset="1" stop-color="#2b5596"/>
    </linearGradient>
    <linearGradient id="frontGrilleTone" x1="0" y1="0" x2="0" y2="1">
      <stop offset="0" stop-color="#c9b08a"/>
      <stop offset=".35" stop-color="#8f7756"/>
      <stop offset=".6" stop-color="#2a2f36"/>
      <stop offset="1" stop-color="#15181d"/>
    </linearGradient>
    <linearGradient id="frontPolishTone" x1="0" y1="0" x2="0" y2="1">
      <stop offset="0" stop-color="#3f74bd"/>
      <stop offset=".4" stop-color="#5d8fa0"/>
      <stop offset=".65" stop-color="#74af57"/>
      <stop offset="1" stop-color="#74af57"/>
    </linearGradient>
  </defs>

  <rect class="paper" width="560" height="1257"/>

  <!-- brand -->
  <circle class="f-green" cx="54" cy="66" r="20"/>
  <text class="wordmark" x="86" y="64">BRIGHTWELL</text>
  <text class="wordmark" x="86" y="88">AUTO CARE</text>
  <text class="tagline" x="86" y="100">PREMIUM STEAM DETAILING &amp; CERAMIC COATING</text>

  <!-- photo panels -->
  <polygon points="317,0 560,0 560,287 370,287 263,102" fill="url(#frontDetailerTone)" role="img" aria-label="Detailer in cap working on a car"/>
  <polygon points="0,120 240,120 342,307 240,500 0,500" fill="url(#frontGrilleTone)" role="img" aria-label="Steam nozzle cleaning a luxury car grille"/>
  <polygon points="377,325 560,325 560,705 377,705 270,512" fill="url(#frontPolishTone)" role="img" aria-label="Detailer polishing a car panel"/>

  <text class="headline" x="34" y="450">GET</text>
  <text class="headline" x="34" y="482">STEAMED!!</text>

  <g class="slogan" text-anchor="end">
    <text x="527" y="574">FALL IN</text>
    <text x="527" y="612">LOVE WITH</text>
    <text x="527" y="649">YOUR CAR</text>
    <text x="527" y="687">AGAIN</text>
  </g>

  <g class="copy">
    <text class="f-green" x="34" y="572">WE USE STEAM TO CLEAN</text>
    <text class="f-green" x="34" y="606">YOUR VEHICLE HELPING</text>
    <text class="f-green" x="34" y="640">SAVE MILLIONS OF GALLONS</text>
    <text class="f-green" x="34" y="674">OF WATER AND PROTECTING</text>
    <text class="f-blue" x="34" y="708">OUR RIVERS, STREAMS AND</text>
    <text class="f-blue" x="34" y="742">LAKES FROM RUNOFF.</text>
  </g>

  <!-- locations bar -->
  <polygon class="f-blue" points="0,777 280,777 309,806 280,835 0,835"/>
  <polygon class="f-green" points="292,777 314,777 343,806 314,835 292,835 321,806"/>
  <polygon class="f-blue" points="322,777 344,777 369,806 344,835 322,835 347,806"/>
  <text class="bar-title" x="63" y="813">OUR LOCATIONS</text>

  <circle class="f-green" cx="485" cy="880" r="36"/>

  <g class="copy" style="font-size:15.5px">
    <text class="f-green" x="34" y="884">1420 CEDAR AVENUE @ THE CEDAR CROSSING</text>
    <text class="f-green" x="34" y="918">SHOPS, BOULDER</text>
    <text class="f-blue" x="34" y="964">58 ASPENGLOW LANE, SNOWMASS VILLAGE</text>
    <text class="f-green" x="34" y="1013">305 BIRCHWOOD RD #12, AVON</text>
  </g>

  <!-- call bar -->
  <polygon class="f-blue" points="190,1076 215,1047 237,1047 212,1076 237,1105 215,1105"/>
  <polygon class="f-green" points="220,1076 245,1047 267,1047 242,1076 267,1105 245,1105"/>
  <polygon class="f-blue" points="282,1047 560,1047 560,1105 282,1105 253,1076"/>
  <g class="bar-small" text-anchor="middle">
    <text x="421" y="1072">CALL FOR INFORMATION</text>
    <text x="421" y="1092">&amp; SCHEDULING:</text>
  </g>

  <g class="copy" style="font-size:16px">
    <text class="f-green" x="38" y="1150">BOULDER  (720) 555-0142</text>
    <text class="f-green" x="305" y="1150">VAIL  (970) 555-0187</text>
    <text class="f-blue" x="38" y="1184">ASPEN/SNOWMASS (970) 555-0163</text>
  </g>

  <rect class="f-green" x="0" y="1218" width="560" height="39"/>
</svg>
</div>

<!-- BACK OF CARD -->
<div class="card card--back">
<svg viewBox="0 0 560 1257" xmlns="http://www.w3.org/2000/svg">
  <defs>
    <linearGradient id="backInteriorBefore" x1="0" y1="0" x2="1" y2="1">
      <stop offset="0" stop-color="#8fc06f"/><stop offset="1" stop-color="#4f7d3b"/>
    </linearGradient>
    <linearGradient id="backInteriorAfter" x1="0" y1="0" x2="1" y2="1">
      <stop offset="0" stop-color="#7fa3cf"/><stop offset="1" stop-color="#2f5a96"/>
    </linearGradient>
    <linearGradient id="backGreyCabin" x1="0" y1="0" x2="1" y2="1">
      <stop offset="0" stop-color="#c8cacc"/><stop offset=".6" stop-color="#55585c"/><stop offset="1" stop-color="#2c2e31"/>
    </linearGradient>
    <linearGradient id="backEngineBefore" x1="0" y1="0" x2="1" y2="1">
      <stop offset="0" stop-color="#6e93c4"/><stop offset="1" stop-color="#2c3f5c"/>
    </linearGradient>
    <linearGradient id="backEngineAfter" x1="0" y1="0" x2="1" y2="1">
      <stop offset="0" stop-color="#9cca7e"/><stop offset="1" stop-color="#3c5a2f"/>
    </linearGradient>
    <linearGradient id="backEngineBay" x1="0" y1="0" x2="1" y2="1">
      <stop offset="0" stop-color="#7b7f85"/><stop offset=".5" stop-color="#303338"/><stop offset="1" stop-color="#1a1c1f"/>
    </linearGradient>
  </defs>

  <rect class="paper" width="560" height="1257"/>

  <!-- brand -->
  <circle class="f-green" cx="198" cy="68" r="20"/>
  <text class="wordmark" x="230" y="66">BRIGHTWELL</text>
  <text class="wordmark" x="230" y="90">AUTO CARE</text>
  <text class="tagline" x="230" y="102">PREMIUM STEAM DETAILING &amp; CERAMIC COATING</text>

  <!-- interior before / after -->
  <polygon points="0,125 199,125 274,260 0,260" fill="url(#backInteriorBefore)" role="img" aria-label="Car interior before steam cleaning"/>
  <polygon points="362,125 560,125 560,260 286,260" fill="url(#backInteriorAfter)" role="img" aria-label="Car interior after steam cleaning"/>
  <polygon points="0,280 274,280 199,414 0,414" fill="url(#backGreyCabin)" role="img" aria-label="Dirty front footwell before cleaning"/>
  <polygon points="286,280 560,280 560,414 362,414" fill="url(#backGreyCabin)" role="img" aria-label="Clean front footwell after cleaning"/>
  <text class="section-title" x="280" y="142" text-anchor="middle">INTERIOR</text>
  <text class="tile-label" x="34" y="158">BEFORE</text>
  <text class="tile-label" x="526" y="158" text-anchor="end">AFTER</text>

  <!-- exterior before / after -->
  <polygon points="0,449 199,449 274,584 0,584" fill="url(#backEngineBefore)" role="img" aria-label="Engine bay before steam cleaning"/>
  <polygon points="362,449 560,449 560,584 286,584" fill="url(#backEngineAfter)" role="img" aria-label="Engine bay after steam cleaning"/>
  <polygon points="0,603 274,603 199,738 0,738" fill="url(#backEngineBay)" role="img" aria-label="Leaf-covered engine before cleaning"/>
  <polygon points="286,603 560,603 560,738 362,738" fill="url(#backEngineBay)" role="img" aria-label="Clean engine after cleaning"/>
  <text class="section-title" x="280" y="466" text-anchor="middle">EXTERIOR</text>
  <text class="tile-label" x="34" y="481">BEFORE</text>
  <text class="tile-label" x="526" y="481" text-anchor="end">AFTER</text>

  <circle class="f-green" cx="280" cy="700" r="30"/>

  <!-- services bar -->
  <polygon class="f-blue" points="0,776 280,776 309,805 280,834 0,834"/>
  <polygon class="f-green" points="292,776 314,776 343,805 314,834 292,834 321,805"/>
  <polygon class="f-blue" points="322,776 344,776 369,805 344,834 322,834 347,805"/>
  <text class="bar-title" x="63" y="812">OUR SERVICES</text>

  <g class="copy" style="font-size:15.8px">
    <text class="f-green" x="34" y="884">PREMIUM STEAM WASHES STARTING AT <tspan class="f-blue price">$100</tspan> AND UP</text>
    <text class="f-blue" x="34" y="933">FULL STEAM DETAILING STARTING AT <tspan class="f-green price">$275</tspan> AND UP</text>
    <text class="f-green" x="34" y="982">HEADLIGHT RESTORATION - <tspan class="f-blue price">$110</tspan></text>
    <text class="f-blue" x="34" y="1031">ENGINE STEAM CLEANING - <tspan class="f-green price">$75</tspan></text>
    <text class="f-green" x="34" y="1081">PAINT CORRECTION (MULTI-STAGE POLISHING)</text>
    <text class="f-green" x="34" y="1116">STARTING AT <tspan class="f-blue price">$650</tspan> AND UP</text>
  </g>

  <text class="section-title" x="280" y="1172" text-anchor="middle" style="font-size:18px">CALL OR VISIT US FOR A QUOTE</text>

  <rect class="f-green" x="0" y="1217" width="560" height="40"/>
</svg>
</div>

</body>
</html>
```